Naturopath Practitioner Card Design

I am a naturopath needing a design for a business card mainly to show that I am a naturopath and have some contact details to give to prospective clients. I am open minded about the design and what is on the second side of the card whether it just be some artwork or space for details, appointment times etc. Naturopathy is the practice of natural medicine that uses a holistic approach and incorporates herbal and nutritional medicine.

Industry/Entity Type

Business

Contact Information for Business Card

Tom Welby NaturopathBHSc (Naturopathy) Member PHRA 0492 815 306 tom.welby@mailbright.com www.tomwelbynaturopathy.com.au

Requirements
Nice to have
• Would prefer some kind of original pattern/art work/logo rather than an image, not fussed if its very simple/basic
• I am open to any colour but think I would prefer a more earthy sandy clay etc type style than the greens that are commonly associated with naturopathy.
Should not have
• Don't really want to have generic stock images on it

```html
<!DOCTYPE html>
<html lang="en">
<head>
<meta charset="utf-8">
<title>Tom Welby Naturopath – Business Cards</title>
<link rel="stylesheet" href="https://fonts.googleapis.com/css2?family=Montserrat:wght@300;400;500&display=swap">
<style>
  :root {
    --page: #ecebe8;
    --card: #ffffff;
    --clay: #9c8a7c;
    --leaf: #8dc63f;
    --ink: #555454;
    --shadow: rgba(60, 50, 40, 0.18);
  }
  * { box-sizing: border-box; margin: 0; padding: 0; }
  html, body {
    width: 1200px;
    height: 799px;
    overflow: hidden;
    background: var(--page);
  }
  .canvas {
    position: relative;
    width: 1200px;
    height: 799px;
  }
  .card {
    position: absolute;
    top: 240px;
    width: 540px;
    height: 310px;
    background: var(--card);
    box-shadow: 0 6px 18px var(--shadow);
  }
  .card--front { left: 40px; }
  .card--back { left: 620px; }

  .card__frame {
    position: absolute;
    inset: 0;
    width: 100%;
    height: 100%;
  }

  .wordmark {
    position: absolute;
    left: 0;
    right: 0;
    text-align: center;
    font-family: "Montserrat", sans-serif;
    font-weight: 400;
    color: var(--clay);
    line-height: 1;
  }
  .card--front .wordmark { top: 116px; }
  .wordmark__name { display: block; font-size: 46px; }
  .wordmark__role { display: block; font-size: 24px; margin-top: 10px; }

  .card--back .wordmark { top: 56px; }
  .card--back .wordmark__name { font-size: 28px; }
  .card--back .wordmark__role { font-size: 15px; margin-top: 6px; }

  .details {
    position: absolute;
    left: 50px;
    right: 36px;
    top: 170px;
    display: flex;
    align-items: flex-start;
  }
  .details__person {
    padding-right: 18px;
    font-family: "Montserrat", sans-serif;
    font-weight: 400;
    font-size: 16px;
    color: var(--ink);
    line-height: 1.3;
  }
  .details__name {
    font-weight: 500;
    font-size: 21px;
    color: var(--clay);
    line-height: 1.2;
    margin-bottom: 3px;
  }
  .details__divider {
    width: 1.5px;
    height: 78px;
    margin-top: 4px;
    background: var(--clay);
  }
  .details__contact {
    padding-left: 16px;
    padding-top: 4px;
    font-family: "Montserrat", sans-serif;
    font-weight: 400;
    font-size: 14px;
    color: var(--ink);
    line-height: 1.6;
    white-space: nowrap;
  }
</style>
</head>
<body>
<main class="canvas">

  <section class="card card--front" aria-label="Business card front">
    <svg class="card__frame" viewBox="0 0 540 310" aria-hidden="true">
      <path d="M16 20 Q120 16 270 18 T524 16 Q527 110 525 200 T522 292 Q400 295 270 293 T18 294 Q15 200 17 120 T16 20 Z"
            fill="none" stroke="var(--clay)" stroke-width="2.5" stroke-linejoin="round"/>
    </svg>
    <div class="wordmark">
      <span class="wordmark__name">Tom Welby</span>
      <span class="wordmark__role">Naturopath</span>
    </div>
  </section>

  <section class="card card--back" aria-label="Business card back">
    <svg class="card__frame" viewBox="0 0 540 310" aria-hidden="true">
      <rect x="14" y="14" width="512" height="282" rx="16" ry="16"
            fill="none" stroke="var(--leaf)" stroke-width="5"/>
    </svg>
    <div class="wordmark">
      <span class="wordmark__name">Tom Welby</span>
      <span class="wordmark__role">Naturopath</span>
    </div>
    <div class="details">
      <div class="details__person">
        <div class="details__name">Tom Welby</div>
        <div>Naturopath BHSc</div>
        <div>Member PHRA</div>
      </div>
      <div class="details__divider"></div>
      <div class="details__contact">
        <div>0492 815 306</div>
        <div>tom.welby@mailbright.com</div>
        <div>www.tomwelbynaturopathy.com.au</div>
      </div>
    </div>
  </section>

</main>
</body>
</html>
```